JT & WE Shearing Pty Ltd

We already have an existing logo created by Lumen Quarry however we have restructured to a company. We would like someone to add Pty Ltd to our business name please.

Colors

Designer to choose only greyscale colors for use in the design.

```html
<!DOCTYPE html>
<html lang="en">
<head>
<meta charset="utf-8">
<title>JT &amp; WE Shearing Pty Ltd – Business Card</title>
<link href="https://fonts.googleapis.com/css2?family=Poppins:wght@400;500;600&display=swap" rel="stylesheet">
<style>
  :root {
    --backdrop: #1a1a1a;
    --card: #232323;
    --card-edge: #2e2e2e;
    --ink: #f2f2f2;
    --ink-soft: #b5b5b5;
    --ink-muted: #8a8a8a;
    --rule: #5a5a5a;
  }
  * { margin: 0; padding: 0; box-sizing: border-box; }
  html, body {
    width: 1200px; height: 800px; overflow: hidden;
    background: var(--backdrop);
    font-family: "Poppins", sans-serif;
  }
  .canvas { position: relative; width: 1200px; height: 800px; }

  .card {
    position: absolute;
    width: 520px; height: 297px;
    background: var(--card);
    border: 1px solid var(--card-edge);
  }
  .card--front { left: 150px; top: 100px; }
  .card--back  { left: 530px; top: 420px; }

  .wordmark {
    display: flex; align-items: center; gap: 10px;
    color: var(--ink);
    font-weight: 600;
    white-space: nowrap;
  }
  .wordmark__dot {
    border-radius: 50%;
    background: var(--ink);
    flex: none;
  }
  .card--front .wordmark {
    position: absolute; left: 50%; top: 50%;
    transform: translate(-50%, -50%);
    font-size: 26px;
  }
  .card--front .wordmark__dot { width: 22px; height: 22px; }

  .card--back .wordmark {
    position: absolute; left: 40px; top: 148px;
    transform: translateY(-50%);
    font-size: 15px; gap: 7px;
  }
  .card--back .wordmark__dot { width: 13px; height: 13px; }

  .divider {
    position: absolute; left: 282px; top: 36px;
    width: 1px; height: 206px;
    background: var(--rule);
  }

  .contact {
    position: absolute; left: 302px; top: 30px;
    color: var(--ink-soft);
  }
  .contact__name { font-size: 17px; font-weight: 500; color: var(--ink-muted); line-height: 1.2; }
  .contact__role { font-size: 11px; color: var(--ink); margin-top: 2px; }
  .contact__address { font-size: 11px; line-height: 1.4; margin-top: 18px; color: var(--ink-soft); }
  .contact__address .company { color: var(--ink-muted); }
  .contact__lines { list-style: none; margin-top: 16px; font-size: 11.5px; color: var(--ink); }
  .contact__lines li { display: flex; align-items: center; gap: 8px; line-height: 1.45; }
  .contact__lines svg { width: 9px; height: 9px; fill: var(--ink-soft); flex: none; }
</style>
</head>
<body>
<main class="canvas">

  <section class="card card--front" aria-label="Card front">
    <div class="wordmark"><span class="wordmark__dot"></span>JT &amp; WE Shearing Pty Ltd</div>
  </section>

  <section class="card card--back" aria-label="Card back">
    <div class="wordmark"><span class="wordmark__dot"></span>JT &amp; WE Shearing Pty Ltd</div>
    <div class="divider"></div>
    <div class="contact">
      <p class="contact__name">Daniel Harper</p>
      <p class="contact__role">President</p>
      <p class="contact__address">
        <span class="company">JT&amp;WE Shearing Pty Ltd</span><br>
        PO Box 415<br>
        Kellerby WA 6402
      </p>
      <ul class="contact__lines">
        <li>
          <svg viewBox="0 0 10 10"><path d="M2 0.5 L3.6 0.5 L4.2 2.8 L3 3.8 Q4 6 6.2 7 L7.2 5.8 L9.5 6.4 L9.5 8 Q9.5 9.5 8 9.5 Q1 9 0.5 2 Q0.5 0.5 2 0.5Z"/></svg>
          Wes 0400 518 274
        </li>
        <li>
          <svg viewBox="0 0 10 10"><path d="M0.5 2 H9.5 V8.5 H0.5Z M1 2.4 L5 5.5 L9 2.4" fill="none" stroke="#b5b5b5" stroke-width="1"/></svg>
          jtweshearing@mailbox.com
        </li>
        <li>
          <svg viewBox="0 0 10 10"><circle cx="5" cy="5" r="4.3" fill="none" stroke="#b5b5b5" stroke-width="1"/><path d="M0.7 5 H9.3 M5 0.7 Q2.5 5 5 9.3 M5 0.7 Q7.5 5 5 9.3" fill="none" stroke="#b5b5b5" stroke-width="0.8"/></svg>
          www.jtweshearing.com
        </li>
      </ul>
    </div>
  </section>

</main>
</body>
</html>
```